Web form face-lift for an online startup

We are a web startup building a SaaS application for the freight industry. The project is mainly dedicated to the paint the main form that our customer are using along the search results that the they get. All details are in the attached documents.
Updates
The application serves the Freight Forwarders community so please think towards this industry when using background images, banners, colors, icons, etc. Computer and technology images are irrelevant.
Customer fields at the top of the page is actually part of the form.
Target Market(s)
Usually business users (Sales people, procurement, shippers, freight forwarders). Some are less tech savvy and some appreciate the new trendy web apps.
Industry/Entity Type
Building
Colors
Designer to choose colors to be used in the design.
Look and feel
Each slider illustrates characteristics of the customer's brand and the style your logo design should communicate.

```html
<!DOCTYPE html>
<html lang="en">
<head>
<meta charset="utf-8">
<title>SAAS application – Search for Quotes</title>
<link rel="stylesheet" href="https://fonts.googleapis.com/css2?family=Montserrat:wght@400;500;600;700&display=swap">
<style>
  :root {
    --bar-dark: #2d2d2d;
    --page-bg: #f3f3f2;
    --text-dark: #222222;
    --text-mid: #555555;
    --text-light: #ffffff;
    --field-border: #cfcfcf;
    --placeholder: #9a9a9a;
    --accent-orange: #f0a326;
    --accent-orange-light: #ffd35a;
    --link-orange: #e8971a;
    --teal: #3d7a89;
    --teal-dark: #2f6472;
    --panel-bg: #ebebeb;
    --select-blue: #2d5f7a;
    --arrow-green: #5fb51f;
    --hazard-red: #d22222;
  }
  * { box-sizing: border-box; margin: 0; padding: 0; }
  html, body { width: 1200px; height: 958px; overflow: hidden; }
  body {
    position: relative;
    background: var(--page-bg);
    font-family: "Montserrat", Arial, sans-serif;
    color: var(--text-dark);
    font-size: 12px;
  }
  .abs { position: absolute; }

  /* header */
  .site-header { position: absolute; left: 0; top: 0; width: 1200px; height: 66px; background: var(--bar-dark); box-shadow: 0 2px 6px rgba(0,0,0,.25); }
  .brand { left: 162px; top: 17px; font-size: 24px; color: var(--text-light); font-weight: 400; letter-spacing: .2px; }
  .brand b { font-weight: 700; }
  .util { top: 10px; font-size: 11px; color: #bbbbbb; }
  .util.user { color: var(--link-orange); }
  .menu-dot { left: 475px; top: 31px; width: 25px; height: 25px; border-radius: 50%; border: 3px solid #6bbfd8; background: #1e1e1e; }
  .menu-item { top: 37px; font-size: 11px; color: var(--text-light); }

  /* form */
  .page-title { left: 162px; top: 95px; font-size: 21px; font-weight: 500; }
  .label { font-size: 11px; font-weight: 600; color: var(--text-dark); }
  .field { background: #fff; border: 1px solid var(--field-border); border-radius: 3px; font-size: 11px; color: var(--placeholder); display: flex; align-items: center; padding-left: 8px; }
  .field.center { justify-content: center; padding-left: 0; }
  .checkbox { width: 13px; height: 13px; border: 1px solid #bdbdbd; background: #fff; border-radius: 2px; }
  .select { background: linear-gradient(#ffffff, #e4e4e4); border: 1px solid #c2c2c2; border-radius: 3px; font-size: 11px; font-weight: 600; color: var(--select-blue); display: flex; align-items: center; justify-content: space-between; padding: 0 8px 0 12px; }
  .select::after { content: ""; border: 4px solid transparent; border-top: 5px solid #666; margin-top: 4px; }

  .cargo-panel { left: 162px; top: 228px; width: 876px; height: 260px; background: var(--panel-bg); border: 1px solid #c9c9c9; border-radius: 3px; overflow: hidden; }
  .panel-tabs { position: absolute; left: 0; top: 0; width: 100%; height: 50px; background: var(--teal); border-bottom: 1px solid var(--teal-dark); }
  .tab { position: absolute; border-radius: 3px 3px 0 0; }
  .tab.active { left: 16px; top: 5px; width: 80px; height: 46px; background: var(--panel-bg); padding: 6px 14px 4px; }
  .tab.idle { top: 12px; height: 38px; background: var(--teal-dark); padding: 4px 6px; }
  .tab-art { width: 100%; height: 100%; border-radius: 2px; }
  .btn-small { background: linear-gradient(var(--accent-orange-light), var(--accent-orange)); border: 1px solid #d68a12; border-radius: 3px; font-size: 10px; font-weight: 600; color: var(--text-dark); display: flex; align-items: center; justify-content: center; }
  .divider { left: 16px; top: 195px; width: 842px; height: 1px; background: #d4d4d4; }

  /* route banner */
  .route-banner { left: 0; top: 535px; width: 1200px; height: 153px; background: linear-gradient(180deg, #3e3d38 0%, #242320 50%, #34332d 100%); }
  .route-label { font-size: 15px; font-weight: 700; color: var(--text-light); }
  .route-field { height: 37px; font-size: 10px; }

  /* options */
  .section-title { left: 162px; top: 723px; font-size: 18px; font-weight: 500; }
  .radio { width: 13px; height: 13px; border: 1px solid #bdbdbd; border-radius: 50%; background: #fff; }
  .opt-text { font-size: 11px; font-weight: 500; }
  .link { color: var(--link-orange); font-weight: 500; }
  .hazard { width: 15px; height: 15px; }
  .btn-search { left: 434px; top: 828px; width: 184px; height: 47px; border-radius: 24px; background: linear-gradient(#ffd65a, #f5a623); border: 1px solid #dc8f14; box-shadow: 0 2px 3px rgba(0,0,0,.2); font-size: 15px; font-weight: 700; color: var(--text-dark); display: flex; align-items: center; justify-content: center; letter-spacing: .3px; }

  /* footer */
  .site-footer { left: 0; top: 915px; width: 1200px; height: 43px; background: var(--bar-dark); }
  .foot-link { top: 14px; font-size: 10px; color: #cfcfcf; }
  .social-dot { top: 14px; width: 15px; height: 15px; border-radius: 50%; background: #8e8e8e; }
</style>
</head>
<body>

<header class="site-header">
  <div class="abs brand"><b>SAAS</b> application</div>
  <div class="abs util" style="left:875px">USD ▾</div>
  <div class="abs util" style="left:919px">English ▾</div>
  <div class="abs util user" style="left:983px">User name</div>
  <div class="abs menu-dot"></div>
  <nav>
    <div class="abs menu-item" style="left:523px">Menu Item 1</div>
    <div class="abs menu-item" style="left:613px">Menu Item 2</div>
    <div class="abs menu-item" style="left:702px">Menu Item 3</div>
    <div class="abs menu-item" style="left:789px">Menu Item 4</div>
    <div class="abs menu-item" style="left:876px">Menu Item 5</div>
    <div class="abs menu-item" style="left:972px">Menu Item 6</div>
  </nav>
</header>

<main>
  <h1 class="abs page-title">Search for Quotes</h1>
  <div class="abs label" style="left:162px;top:150px">Customer</div>
  <div class="abs field" style="left:223px;top:138px;width:390px;height:37px"></div>
  <div class="abs checkbox" style="left:162px;top:185px"></div>
  <div class="abs label" style="left:181px;top:185px">Rate Quote?</div>

  <section class="abs cargo-panel">
    <div class="panel-tabs">
      <div class="tab active"><div class="tab-art" role="img" aria-label="Cardboard box" style="background:linear-gradient(#d9b47e,#b88950)"></div></div>
      <div class="tab idle" style="left:84px;width:64px"><div class="tab-art" role="img" aria-label="Shipping container" style="background:linear-gradient(#4fa24a,#2c6f2b)"></div></div>
      <div class="tab idle" style="left:152px;width:62px"><div class="tab-art" role="img" aria-label="Wrapped parcel" style="background:linear-gradient(#e45a7a,#b92b4c)"></div></div>
      <div class="abs btn-small" style="left:807px;top:14px;width:54px;height:22px">+ more</div>
    </div>

    <div class="abs label" style="left:15px;top:80px">Qty</div>
    <div class="abs label" style="left:93px;top:80px">Stackabel</div>
    <div class="abs label" style="left:164px;top:80px">Load</div>
    <div class="abs label" style="left:365px;top:80px">Length</div>
    <div class="abs label" style="left:440px;top:80px">Width</div>
    <div class="abs label" style="left:514px;top:80px">Height</div>
    <div class="abs label" style="left:653px;top:80px">Weight</div>

    <div class="abs field center" style="left:14px;top:96px;width:62px;height:31px">5</div>
    <div class="abs checkbox" style="left:117px;top:106px;width:11px;height:11px"></div>
    <div class="abs select" style="left:163px;top:96px;width:185px;height:31px">Box/Pallet</div>
    <div class="abs field center" style="left:363px;top:96px;width:61px;height:31px">100</div>
    <div class="abs field center" style="left:438px;top:96px;width:60px;height:31px">100</div>
    <div class="abs field center" style="left:512px;top:96px;width:61px;height:31px">100</div>
    <div class="abs select" style="left:590px;top:96px;width:46px;height:31px;padding:0 6px">Cm</div>
    <div class="abs field" style="left:653px;top:96px;width:166px;height:31px;border-radius:3px 0 0 3px">Box/Pallet</div>
    <div class="abs select" style="left:818px;top:96px;width:41px;height:31px;padding:0 6px;border-radius:0 3px 3px 0">Kg</div>

    <div class="abs btn-small" style="left:16px;top:152px;width:108px;height:28px">+ Add more units</div>
    <div class="abs divider"></div>

    <div class="abs label" style="left:397px;top:221px;font-weight:500">Total</div>
    <div class="abs field center" style="left:433px;top:213px;width:62px;height:30px">5</div>
    <div class="abs field" style="left:511px;top:213px;width:115px;height:30px;border-radius:3px 0 0 3px">1</div>
    <div class="abs select" style="left:625px;top:213px;width:51px;height:30px;padding:0 6px;border-radius:0 3px 3px 0">CBM</div>
    <div class="abs field" style="left:694px;top:213px;width:125px;height:30px;border-radius:3px 0 0 3px">100</div>
    <div class="abs select" style="left:818px;top:213px;width:41px;height:30px;padding:0 6px;border-radius:0 3px 3px 0">Kg</div>
  </section>

  <section class="abs route-banner" role="img" aria-label="Container terminal with stacked shipping containers at dusk"></section>
  <div class="abs route-label" style="left:162px;top:601px">From:</div>
  <div class="abs field route-field" style="left:212px;top:593px;width:343px">Shipping address or port</div>
  <svg class="abs" style="left:599px;top:600px" width="32" height="24" viewBox="0 0 32 24" aria-hidden="true">
    <path d="M0 7h16V0l16 12-16 12v-7H0z" fill="var(--arrow-green)"/>
  </svg>
  <div class="abs route-label" style="left:666px;top:601px">To:</div>
  <div class="abs field route-field" style="left:694px;top:593px;width:343px">Shipping address or port</div>

  <h2 class="abs section-title">Options</h2>
  <div class="abs radio" style="left:162px;top:756px"></div>
  <div class="abs opt-text" style="left:182px;top:756px">Import</div>
  <div class="abs radio" style="left:238px;top:756px"></div>
  <div class="abs opt-text" style="left:258px;top:756px">Export</div>
  <div class="abs opt-text" style="left:314px;top:756px">Incoterm: <span class="link">FCA</span></div>

  <div class="abs checkbox" style="left:522px;top:757px"></div>
  <svg class="abs hazard" style="left:540px;top:755px" viewBox="0 0 16 16" aria-hidden="true"><circle cx="8" cy="8" r="6.5" fill="#222" stroke="var(--hazard-red)" stroke-width="2"/></svg>
  <div class="abs checkbox" style="left:579px;top:757px"></div>
  <svg class="abs hazard" style="left:597px;top:755px" viewBox="0 0 16 16" aria-hidden="true"><circle cx="8" cy="8" r="6.5" fill="#222" stroke="var(--hazard-red)" stroke-width="2"/></svg>
  <div class="abs checkbox" style="left:632px;top:757px"></div>
  <svg class="abs hazard" style="left:650px;top:755px" viewBox="0 0 16 16" aria-hidden="true"><circle cx="8" cy="8" r="6.5" fill="#fff" stroke="var(--hazard-red)" stroke-width="2"/><circle cx="8" cy="8" r="2.5" fill="#222"/></svg>

  <div class="abs select" style="left:813px;top:748px;width:224px;height:29px;color:var(--text-dark);font-weight:500">Price Level</div>
  <div class="abs opt-text link" style="left:955px;top:784px;font-weight:600">More Options</div>

  <div class="abs btn-search">SEARCH QUOTES</div>
  <div class="abs opt-text" style="left:628px;top:846px;font-weight:600">or</div>
  <div class="abs opt-text link" style="left:647px;top:846px">Create Manually</div>
</main>

<footer class="abs site-footer">
  <div class="abs foot-link" style="left:162px">About Us</div>
  <div class="abs foot-link" style="left:222px">Privacy policy</div>
  <div class="abs foot-link" style="left:308px">Terms of Service</div>
  <div class="abs foot-link" style="left:407px">News</div>
  <div class="abs social-dot" style="left:925px"></div>
  <div class="abs social-dot" style="left:949px"></div>
  <div class="abs social-dot" style="left:973px"></div>
  <div class="abs social-dot" style="left:997px"></div>
  <div class="abs social-dot" style="left:1021px"></div>
</footer>

</body>
</html>
```